Coffee 817 V-Pod

We have recently launched a coffee company called Cafe 817 that provides clean water and economic empowerment to Hondurans. It is premium direct trade coffee. We are looking for a very clean, professional looking box for our V-Pods. I'm uploading a logo, what we are thinking so far, and an example of a bramble loaf v pod box that I liked, but if you can think of a better design, please submit it. I'm not tied to anything that I uploaded. Please submit the artwork in a similiar format to diagram with the outline of the print out.

```html
<!DOCTYPE html>
<html lang="en">
<head>
<meta charset="utf-8">
<title>Cafe 817 V-Pod Box Dieline</title>
<link rel="stylesheet" href="https://fonts.googleapis.com/css2?family=Poppins:wght@500;600;800&family=Roboto:wght@400;500&display=swap">
<style>
  :root {
    --paper: #ffffff;
    --cut: #111111;
    --crease: #e01b1b;
    --dim: #1a1ae6;
    --brand: #0d2a6b;
    --sky: #1aa2f2;
    --navy: #0d2a6b;
    --deep: #0a2d6a;
    --teal: #0b90c3;
    --wave: #3a62cc;
    --sun: #fdd43a;
    --sun-deep: #f6c21d;
    --pink: #ea3d8c;
    --plum: #5b2a86;
    --strip: #1f3559;
  }
  html, body {
    margin: 0;
    width: 1200px;
    height: 1200px;
    overflow: hidden;
    background: var(--paper);
  }
  .dieline { display: block; width: 1200px; height: 1200px; }
  .cut { fill: none; stroke: var(--cut); stroke-width: 2; }
  .crease { fill: none; stroke: var(--crease); stroke-width: 2; }
  .crease-dash { fill: none; stroke: var(--crease); stroke-width: 2; stroke-dasharray: 10 8; }
  .perf { fill: none; stroke: var(--cut); stroke-width: 1.5; stroke-dasharray: 3 3; }
  .dim-line { fill: none; stroke: var(--dim); stroke-width: 2; }
  .dim-text { fill: var(--dim); font-family: "Roboto", sans-serif; font-size: 22px; font-weight: 500; }
  .dim-frac { font-size: 13px; }
  .job-code { fill: var(--dim); font-family: "Roboto", sans-serif; font-size: 15px; }
  .brand-name { fill: var(--brand); font-family: "Poppins", sans-serif; font-weight: 600; font-size: 36px; }
  .serial-label { fill: #ffffff; font-family: "Roboto", sans-serif; font-size: 9px; }
  .roast-label { fill: #ffffff; font-family: "Poppins", sans-serif; font-weight: 600; font-size: 22px; }
  .count-label { fill: #ffffff; font-family: "Poppins", sans-serif; font-weight: 800; font-size: 28px; }
  .count-number { fill: #ffffff; font-family: "Poppins", sans-serif; font-weight: 800; font-size: 44px; }
</style>
</head>
<body>
<svg class="dieline" viewBox="0 0 1500 1500" xmlns="http://www.w3.org/2000/svg">
  <defs>
    <linearGradient id="side-left" x1="0" y1="0" x2="1" y2="1">
      <stop offset="0" stop-color="var(--sky)"/>
      <stop offset="1" stop-color="var(--navy)"/>
    </linearGradient>
    <linearGradient id="front-waves" x1="0" y1="0" x2="0" y2="1">
      <stop offset="0" stop-color="var(--wave)"/>
      <stop offset="0.22" stop-color="#dfe6f7"/>
      <stop offset="0.35" stop-color="#ffffff"/>
      <stop offset="0.68" stop-color="#ffffff"/>
      <stop offset="0.82" stop-color="#c9d5f2"/>
      <stop offset="1" stop-color="#2a4aa6"/>
    </linearGradient>
    <linearGradient id="side-right" x1="0" y1="0" x2="0.3" y2="1">
      <stop offset="0" stop-color="var(--deep)"/>
      <stop offset="1" stop-color="var(--teal)"/>
    </linearGradient>
    <radialGradient id="back-burst" cx="0.5" cy="0.5" r="0.7">
      <stop offset="0" stop-color="#ffe680"/>
      <stop offset="1" stop-color="var(--sun-deep)"/>
    </radialGradient>
  </defs>

  <g class="panels">
    <rect x="32" y="386" width="244" height="372" fill="url(#side-left)" role="img" aria-label="Angular blue faceted background"/>
    <rect class="serial-strip" x="254" y="632" width="22" height="126" fill="var(--strip)"/>
    <text class="serial-label" transform="translate(269,730) rotate(-90)">SERIAL CODES</text>

    <rect x="276" y="386" width="487" height="372" fill="url(#front-waves)" role="img" aria-label="Flowing blue wave background framing the brand name"/>
    <rect x="488" y="532" width="36" height="36" fill="var(--brand)"/>
    <text class="brand-name" x="506" y="645" text-anchor="middle">Cafe 817</text>

    <rect x="763" y="386" width="244" height="372" fill="url(#side-right)" role="img" aria-label="Layered deep blue to teal geometric background"/>

    <rect x="1007" y="386" width="475" height="372" fill="url(#back-burst)" role="img" aria-label="Yellow sunburst background with stars"/>
    <circle cx="1245" cy="585" r="160" fill="none" stroke="#b9d6e0" stroke-width="4"/>
    <g transform="rotate(-12 1220 512)">
      <rect x="1125" y="490" width="190" height="44" rx="22" fill="var(--plum)"/>
      <text class="roast-label" x="1220" y="520" text-anchor="middle">Medium Dark</text>
    </g>
    <g transform="rotate(-12 1240 610)">
      <rect x="1070" y="552" width="340" height="105" fill="var(--pink)"/>
      <text class="count-label" x="1240" y="598" text-anchor="middle">Single Served Pods</text>
      <text class="count-number" x="1240" y="643" text-anchor="middle">50</text>
    </g>
  </g>

  <g class="cuts">
    <path class="cut" d="M32,386 L160,259 L271,259 L281,386"/>
    <path class="cut" d="M32,758 L32,850 L39,857 L46,939 L272,939 L279,857 L286,850 L286,758"/>
    <path class="cut" d="M303,370 L291,356 L291,221 L378,221 L415,259 L522,259 L522,246 L549,221 L741,221 L755,386"/>
    <path class="cut" d="M281,386 L291,376"/>
    <rect class="cut" x="287" y="758" width="468" height="257"/>
    <path class="cut" d="M757,386 L884,259 L997,259 L1007,386"/>
    <path class="cut" d="M757,758 L757,850 L764,857 L764,880 L1002,880 L1004,857 L1011,850 L1011,758"/>
    <path class="cut" d="M1030,370 L1017,356 L1017,221 L1103,221 L1140,259 L1248,259 L1248,246 L1275,221 L1467,221 L1482,386"/>
    <path class="cut" d="M1007,386 L1017,376"/>
    <rect class="cut" x="1013" y="758" width="468" height="257"/>
    <path class="cut" d="M1482,392 Q1494,392 1500,398 M1482,752 Q1494,752 1500,746"/>
  </g>

  <g class="folds">
    <path class="crease" d="M32,386 L276,386 M763,386 L1007,386 M287,758 L763,758 M1140,758 L1482,758"/>
    <path class="crease-dash" d="M303,370 L415,259 M1030,370 L1140,259"/>
    <path class="perf" d="M604,758 L604,1015 M1163,758 L1163,1015"/>
  </g>

  <text class="job-code" transform="translate(470,279) rotate(180)" text-anchor="middle">H.10.018</text>

  <g class="dimensions">
    <path class="dim-line" d="M0,221 L280,221 M0,386 L20,386 M0,758 L20,758 M0,939 L35,939 M1478,221 L1500,221 M1490,386 L1500,386 M1490,758 L1500,758 M1490,1015 L1500,1015"/>

    <path class="dim-line" d="M604,1025 L604,1078 M755,1025 L755,1078 M604,1073 L755,1073"/>
    <path class="dim-line" d="M1013,1025 L1013,1078 M1163,1025 L1163,1078 M1013,1073 L1163,1073"/>
    <path class="dim-line" d="M32,1103 L32,1170 M287,1103 L287,1170 M755,1103 L755,1170 M1013,1103 L1013,1170 M1481,1103 L1481,1170 M32,1163 L1500,1163"/>
    <path class="dim-line" d="M32,1255 L32,1270 M32,1262 L1500,1262"/>

    <g fill="var(--dim)">
      <path d="M604,1073 l14,-4 v8z M755,1073 l-14,-4 v8z M1013,1073 l14,-4 v8z M1163,1073 l-14,-4 v8z"/>
      <path d="M32,1163 l18,-5 v10z M287,1163 l-18,-5 v10z M287,1163 l18,-5 v10z M755,1163 l-18,-5 v10z M755,1163 l18,-5 v10z M1013,1163 l-18,-5 v10z M1013,1163 l18,-5 v10z M1481,1163 l-18,-5 v10z"/>
      <path d="M32,1262 l18,-5 v10z"/>
    </g>

    <g class="dim-labels">
      <rect x="660" y="1060" width="40" height="26" fill="var(--paper)"/>
      <text class="dim-text" transform="translate(680,1066) rotate(180)" text-anchor="middle">2<tspan class="dim-frac">1/2</tspan></text>
      <rect x="1068" y="1060" width="40" height="26" fill="var(--paper)"/>
      <text class="dim-text" transform="translate(1088,1066) rotate(180)" text-anchor="middle">2<tspan class="dim-frac">1/2</tspan></text>

      <rect x="125" y="1148" width="66" height="30" fill="var(--paper)"/>
      <text class="dim-text" transform="translate(158,1156) rotate(180)" text-anchor="middle">4<tspan class="dim-frac">7/32</tspan></text>
      <rect x="495" y="1148" width="54" height="30" fill="var(--paper)"/>
      <text class="dim-text" transform="translate(522,1156) rotate(180)" text-anchor="middle">7<tspan class="dim-frac">3/4</tspan></text>
      <rect x="857" y="1148" width="54" height="30" fill="var(--paper)"/>
      <text class="dim-text" transform="translate(884,1156) rotate(180)" text-anchor="middle">4<tspan class="dim-frac">1/4</tspan></text>
      <rect x="1220" y="1148" width="54" height="30" fill="var(--paper)"/>
      <text class="dim-text" transform="translate(1247,1156) rotate(180)" text-anchor="middle">7<tspan class="dim-frac">3/4</tspan></text>

      <rect x="705" y="1246" width="92" height="32" fill="var(--paper)"/>
      <text class="dim-text" transform="translate(751,1255) rotate(180)" text-anchor="middle">24<tspan class="dim-frac">19/32</tspan></text>
    </g>
  </g>
</svg>
</body>
</html>
```